Korimo Business Cards

Korimo is a software startup and we are looking for business cards that help convey our employee personalities, as well as the professionalism of the company.
Our company font is Comfortaa - and the company logo is attached (we are okay having the text beside the logo if applicable) where we can find the company colour scheme. Cards can be horizontal or vertical format.
We are looking for a two sided business card - on the front we will see the personal details of the employee (name, position, email and phone number), and then on the back, we will see the business details (name and logo, address, phone number, website, email, company tagline: "Building smarter software for every road ahead of us")
We want the design to be clean and simple, but also fun, modern, and capturing of a young startup vibe.

```html
<!DOCTYPE html>
<html lang="en">
<head>
<meta charset="utf-8">
<title>Korimo Business Cards</title>
<link rel="stylesheet" href="https://fonts.googleapis.com/css2?family=Montserrat:ital,wght@0,400;0,700;1,400&display=swap">
<style>
  :root {
    --page: #2b2b2b;
    --card: #1b1b1c;
    --indigo: #5a4fb2;
    --violet: #8a67c2;
    --pink: #c452a4;
    --white: #f4f2f6;
    --grad: linear-gradient(90deg, var(--pink), var(--violet));
  }
  * { box-sizing: border-box; margin: 0; padding: 0; }
  html, body {
    width: 1200px; height: 1200px; overflow: hidden;
    background: var(--page);
    font-family: "Montserrat", sans-serif;
    color: var(--white);
  }
  .card {
    position: absolute; left: 150px;
    width: 900px; height: 514px;
    background: var(--card);
    border-radius: 26px;
    overflow: hidden;
  }
  .card--front { top: 56px; }
  .card--back { top: 630px; }

  .brand { display: flex; align-items: center; gap: 22px; }
  .brand__dot { width: 84px; height: 84px; border-radius: 50%; background: var(--violet); }
  .brand__name {
    font-family: "Montserrat", sans-serif; font-weight: 700;
    font-size: 92px; letter-spacing: 1px; color: var(--indigo); line-height: 1;
  }

  .card--front .brand { position: absolute; left: 90px; top: 80px; }
  .person { position: absolute; left: 96px; top: 236px; }
  .person__name { font-weight: 700; font-size: 40px; letter-spacing: 2px; color: var(--pink); }
  .person__role { font-size: 24px; margin-top: 6px; }
  .contacts--front { position: absolute; left: 96px; top: 360px; display: flex; gap: 44px; font-size: 28px; }

  .contact { display: flex; align-items: center; gap: 12px; white-space: nowrap; }
  .contact svg { flex: none; fill: var(--pink); }

  .edge-strip { position: absolute; left: 0; right: 0; bottom: 0; height: 14px; background: var(--grad); }

  .card--back .brand { position: absolute; left: 50%; top: 120px; transform: translateX(-50%); }
  .contacts--back {
    position: absolute; left: 0; right: 0; top: 300px;
    display: flex; flex-direction: column; align-items: center; gap: 14px; font-size: 21px;
  }
  .contacts--back .row { display: flex; gap: 28px; }
  .tagline-band {
    position: absolute; left: 0; right: 0; bottom: 0; height: 72px;
    background: var(--grad);
    display: flex; align-items: center; justify-content: center;
    font-style: italic; font-size: 26px; color: var(--white);
    white-space: nowrap;
  }
</style>
</head>
<body>

<section class="card card--front">
  <div class="brand">
    <span class="brand__dot"></span>
    <span class="brand__name">korimo</span>
  </div>
  <div class="person">
    <p class="person__name">LIAM CARTER</p>
    <p class="person__role">CEO/Founder</p>
  </div>
  <div class="contacts--front">
    <span class="contact">
      <svg width="26" height="26" viewBox="0 0 24 24"><path d="M6.6 10.8a15 15 0 0 0 6.6 6.6l2.2-2.2a1 1 0 0 1 1-.25 11.4 11.4 0 0 0 3.6.6 1 1 0 0 1 1 1V20a1 1 0 0 1-1 1A17 17 0 0 1 3 4a1 1 0 0 1 1-1h3.5a1 1 0 0 1 1 1c0 1.25.2 2.45.6 3.6a1 1 0 0 1-.25 1z"/></svg>
      +123.555.0142
    </span>
    <span class="contact">
      <svg width="26" height="26" viewBox="0 0 24 24"><path d="M2 5h20v14H2z M2 5l10 8 10-8" /></svg>
      liam@korimo.com.au
    </span>
  </div>
  <div class="edge-strip"></div>
</section>

<section class="card card--back">
  <div class="brand">
    <span class="brand__dot"></span>
    <span class="brand__name">korimo</span>
  </div>
  <div class="contacts--back">
    <span class="contact">
      <svg width="20" height="20" viewBox="0 0 24 24"><path d="M12 2a7 7 0 0 0-7 7c0 5 7 13 7 13s7-8 7-13a7 7 0 0 0-7-7zm0 9.5A2.5 2.5 0 1 1 12 6.5a2.5 2.5 0 0 1 0 5z"/></svg>
      Elmwood, Harbour Crescent Park, 2041
    </span>
    <div class="row">
      <span class="contact">
        <svg width="20" height="20" viewBox="0 0 24 24"><path d="M6.6 10.8a15 15 0 0 0 6.6 6.6l2.2-2.2a1 1 0 0 1 1-.25 11.4 11.4 0 0 0 3.6.6 1 1 0 0 1 1 1V20a1 1 0 0 1-1 1A17 17 0 0 1 3 4a1 1 0 0 1 1-1h3.5a1 1 0 0 1 1 1c0 1.25.2 2.45.6 3.6a1 1 0 0 1-.25 1z"/></svg>
        +987.555.0198
      </span>
      <span class="contact">
        <svg width="20" height="20" viewBox="0 0 24 24"><path d="M2 5h20v14H2z M2 5l10 8 10-8"/></svg>
        service@korimo.com.au
      </span>
      <span class="contact">
        <svg width="20" height="20" viewBox="0 0 24 24"><circle cx="12" cy="12" r="10"/><path d="M2 12h20M12 2c3 3 3 17 0 20M12 2c-3 3-3 17 0 20" stroke="#1b1b1c" stroke-width="1.4" fill="none"/></svg>
        www.korimo.com.au
      </span>
    </div>
  </div>
  <div class="tagline-band">“Building smarter software for every road ahead of us”</div>
</section>

</body>
</html>
```